ecommerce news podcast artwork

Podcast cover art for a podcast featuring daily news and events around ecommerce product businesses.

text to be: TILLWIRE
optional third line of text with smaller font: Podcast

looking for something that pops with a medium to light blue background. text can be in white/red/orange colors. prefer solid colors for text, but background can vary.
I'm really open to other ideas too, sometimes you don't know what you want until you see it.

Target Market(s)

ecommerce business owners, managers

Industry/Entity Type

news, business, ecommerce

Font styles to use
Sans Serif

Colors
0054AA
0677BA
7BADD7
CADEEF
E8F1F8
0094D4
00A9DD
6FCCEA
C7EBF8
E9F6FB
F0912C
F2A743
F7CA91
FBE8D2
FDF5EE
EB3D1F
EC4F4E
F09395
F8D3D4
FCEDEE

Requirements
Must have
• text: TILLWIRE
Should not have
• no microphones, headsets/headphones, speakers, or other props like that.

```html
<!DOCTYPE html>
<html lang="en">
<head>
<meta charset="utf-8">
<title>TILLWIRE Podcast – Cover Variations</title>
<link rel="stylesheet" href="https://fonts.googleapis.com/css2?family=Montserrat:wght@600;700&display=swap">
<style>
  :root {
    --sheet-bg: #ffffff;
    --label-bg: #111111;
    --label-text: #ffffff;
    --cream: #FDF5EE;
    --red: #EB3D1F;
    --ink: #1a1a1a;
    --white: #ffffff;
    --sky-top: #0080FF;
    --sky-mid: #2E9BF5;
    --sky-bottom: #C7EFFB;
    --ocean-top: #3AA6DA;
    --ocean-mid: #1A7CC6;
    --ocean-bottom: #0A3F9E;
    --mist-top: #2E7FC8;
    --mist-mid: #7BC3E8;
    --mist-glow: #E9F9FC;
    --podcast-navy: #0C4C9A;
  }
  * { margin: 0; padding: 0; box-sizing: border-box; }
  html, body {
    width: 1200px;
    height: 1200px;
    overflow: hidden;
    background: var(--sheet-bg);
    font-family: "Montserrat", Arial, sans-serif;
  }
  .sheet { position: relative; width: 1200px; height: 1200px; }
  .cover {
    position: absolute;
    width: 480px;
    height: 480px;
    overflow: hidden;
  }
  .cover--a { left: 81px;  top: 90px; }
  .cover--b { left: 605px; top: 90px; }
  .cover--c { left: 81px;  top: 632px; }
  .cover--d { left: 605px; top: 632px; }

  .cover--cream { background: var(--cream); }
  .cover--sky {
    background: linear-gradient(180deg, var(--sky-top) 0%, var(--sky-mid) 45%, #6FCCEA 80%, var(--sky-bottom) 100%);
  }
  .cover--ocean {
    background:
      linear-gradient(125deg, transparent 20%, rgba(120,210,240,0.35) 32%, transparent 45%),
      linear-gradient(180deg, var(--ocean-top) 0%, var(--ocean-mid) 55%, var(--ocean-bottom) 100%);
  }
  .cover--mist {
    background:
      radial-gradient(ellipse 70% 55% at 50% 85%, var(--mist-glow) 0%, rgba(233,249,252,0.6) 40%, transparent 80%),
      linear-gradient(180deg, var(--mist-top) 0%, var(--mist-mid) 55%, #BDE6F5 100%);
  }

  .wordmark {
    position: absolute;
    left: 0; right: 0;
    top: 240px;
    transform: translateY(-50%);
    text-align: center;
    font-weight: 700;
    font-size: 50px;
    letter-spacing: 1px;
  }
  .podcast-line {
    position: absolute;
    left: 67px;
    width: 346px;
    top: 425px;
    display: flex;
    justify-content: space-between;
    font-weight: 600;
    font-size: 10px;
  }
  .tone-red { color: var(--red); }
  .tone-white { color: var(--white); }
  .tone-ink { color: var(--ink); }
  .tone-navy { color: var(--podcast-navy); }

  .variant-label {
    position: absolute;
    width: 42px;
    height: 22px;
    background: var(--label-bg);
    color: var(--label-text);
    font-weight: 700;
    font-size: 13px;
    line-height: 22px;
    text-align: center;
    clip-path: polygon(0 0, 80% 0, 100% -30%, 100% 100%, 0 100%);
  }
  .variant-label--a { left: 519px;  top: 576px; }
  .variant-label--b { left: 1043px; top: 576px; }
  .variant-label--c { left: 519px;  top: 1118px; }
  .variant-label--d { left: 1043px; top: 1118px; }
</style>
</head>
<body>
<main class="sheet">
  <section class="cover cover--a cover--cream">
    <h1 class="wordmark tone-red">TILLWIRE</h1>
    <p class="podcast-line tone-ink"><span>P</span><span>O</span><span>D</span><span>C</span><span>A</span><span>S</span><span>T</span></p>
  </section>
  <div class="variant-label variant-label--a">01</div>

  <section class="cover cover--b cover--sky">
    <h1 class="wordmark tone-white">TILLWIRE</h1>
    <p class="podcast-line tone-navy"><span>P</span><span>O</span><span>D</span><span>C</span><span>A</span><span>S</span><span>T</span></p>
  </section>
  <div class="variant-label variant-label--b">02</div>

  <section class="cover cover--c cover--ocean">
    <h1 class="wordmark tone-white">TILLWIRE</h1>
    <p class="podcast-line tone-white"><span>P</span><span>O</span><span>D</span><span>C</span><span>A</span><span>S</span><span>T</span></p>
  </section>
  <div class="variant-label variant-label--c">03</div>

  <section class="cover cover--d cover--mist">
    <h1 class="wordmark tone-red">TILLWIRE</h1>
    <p class="podcast-line tone-red"><span>P</span><span>O</span><span>D</span><span>C</span><span>A</span><span>S</span><span>T</span></p>
  </section>
  <div class="variant-label variant-label--d">04</div>
</main>
</body>
</html>
```